Red Panda Bamboo Project Postcard Design

My name is Willow Wes.I have been supplying bamboo branches and leaves to a number of zoos including Harrowgate Faunal (Elmcrest Menagerie), Marlow Faunal Society, Quarry Dell Zoo, Fenwick Hill Zoo and ZooKestrel, among others.I also supply bamboo plants to zoos that want to grow bamboo to feed their animals. The bamboo we supply is used predominantly to feed the red pandas.Side note, according to the NFK Ember Fox Lineage Care Plan in section 5, which addresses nutritional requirements, there is a list of bamboo species that are fed to red pandas on page 20. This is a care plan for red pandas which is used by the zoos that belong to the National Faunal Keepers, among others.I have been harvesting and shipping a number of these varieties to many zoos with great results and outstanding feedback, and, since 65%-75% of a red panda’s diet should consist of bamboo, I would like to make your NFK members (and Canadian zoos as well) aware that we strip and ship bamboo branches and leaves within 2 hours of harvest. Typically the bamboo is shipped by SWIFTCART Road and delivered within a few days, depending on distance and urgency. Additionally, we ship or deliver (depending on distance) bamboo plants to zoos that are looking to create a bamboo farm onsite.To give you a little history, I was contacted by Marlow Faunal Society almost a year ago, when they became dissatisfied with the product/services of their previous bamboo supplier. We began supplying MFS, and soon the word spread to other zoos about the quality of the bamboo and the customer service we pride ourselves on, and we received requests to supply them with fresh, high quality bamboo to feed their red pandas and other animals, too. Most of our business in this sector is by word of mouth...We are members of NFK, which is where we want to start with the post card campaign, as well as the Grassland Cane Guild, Federation of Menagerie Gardeners and numerous other organizations.We have a few pictures of red pandas eating the bamboo that I supply, but want to send out a mind blowing postcard to all zoos to promote new business.By the way, my company, Feel the Loam, is the foremost supplier of live bamboo for residential and commercial applications, both indoor and outdoor. We install, remove, maintain bamboo, supply bamboo branches and leaves to zoos for animal feed, and we offer consulting services. Our website, icanecrafter.example, will explain this in more detail.Would like to have pictures of red pandas on the front, or maybe just one incredible one, but we are open to any and all ideas. I have attached a picture that we already have of Pim and Roki with my bamboo, which can be incorporated or not... On the back of the card, I would like to have my logo picture, also attached, to the left of the address section.

Target Market(s)

Zoos: Animal Curators and Caretakers, Nutritionists

Font styles to use
Other font styles liked:
• bamboo letters, is there such a font, or papyrus

Requirements
Must have
• Data from the NFK Ember Fox Lineage Care Plan (Registered document)
Incredible pics of bamboo, red pandas, red pandas eating bamboo, even other animals eating and/or hanging out with bamboo.
Willow Wes's picture on back of card with mailing address below. Logo.
A call to action, ie., call for more information...
Nice to have
• A catchy tag line would be awesome.
Stripped and shipped super-fresh (?)
Maybe, can we superimpose a red panda next to Willow Wes in his picture?
Open to ideas... Maybe 10% off your first order...
Should not have
• Not sure.
You probably know better.

```html
<!DOCTYPE html>
<html lang="en">
<head>
<meta charset="utf-8">
<title>Willow Wes — Postcard</title>
<link href="https://fonts.googleapis.com/css2?family=Roboto+Condensed:wght@400;700&family=Arimo:wght@400;700&display=swap" rel="stylesheet">
<style>
  :root {
    --page: #e9ebe6;
    --leaf-light: #eef6df;
    --leaf-mid: #cfe8a8;
    --leaf-deep: #8cc63f;
    --leaf-dark: #4f8a1e;
    --ink: #1f2a16;
    --ink-soft: #3b4432;
    --white: #ffffff;
    --line: #9aa08f;
    --panda: #a5502a;
    --panda-dark: #5a3220;
    --photo-green: #6f8f4a;
  }
  * { box-sizing: border-box; margin: 0; padding: 0; }
  html, body { width: 900px; height: 1200px; overflow: hidden; }
  body {
    background: var(--page);
    font-family: "Arimo", Arial, sans-serif;
    color: var(--ink);
    position: relative;
  }
  .card {
    position: absolute;
    left: 40px;
    width: 820px;
    height: 540px;
    overflow: hidden;
    box-shadow: 0 6px 18px rgba(0,0,0,.25);
  }
  /* ---------- Front ---------- */
  .card-front {
    top: 36px;
    background: radial-gradient(ellipse at 50% 45%, var(--white) 0%, var(--leaf-light) 55%, var(--leaf-mid) 100%);
  }
  .leaf-border {
    position: absolute;
    inset: 0;
    background:
      radial-gradient(ellipse 180px 110px at 0 0, rgba(79,138,30,.55), transparent 70%),
      radial-gradient(ellipse 200px 120px at 100% 0, rgba(79,138,30,.5), transparent 70%),
      radial-gradient(ellipse 260px 120px at 0 100%, rgba(79,138,30,.55), transparent 70%),
      radial-gradient(ellipse 260px 120px at 100% 100%, rgba(79,138,30,.55), transparent 70%);
  }
  .brand-front {
    position: absolute;
    top: 46px;
    right: 62px;
    display: flex;
    align-items: center;
    gap: 10px;
  }
  .brand-mark {
    width: 22px;
    height: 22px;
    background: var(--leaf-dark);
  }
  .brand-name {
    font-family: "Roboto Condensed", Arial, sans-serif;
    font-weight: 700;
    font-size: 34px;
    color: var(--leaf-dark);
  }
  .tagline {
    position: absolute;
    top: 176px;
    left: 0;
    width: 100%;
    text-align: center;
    font-family: "Roboto Condensed", Arial, sans-serif;
    font-weight: 700;
    font-size: 40px;
    line-height: 1.1;
    color: var(--ink);
  }
  .photo {
    position: absolute;
    border: 4px solid var(--white);
    box-shadow: 0 2px 6px rgba(0,0,0,.3);
  }
  .photo-panda-front {
    left: 158px; top: 296px; width: 196px; height: 146px;
    background: radial-gradient(circle at 50% 45%, var(--panda) 0%, var(--panda-dark) 60%, var(--photo-green) 100%);
  }
  .photo-feeding {
    left: 600px; top: 272px; width: 170px; height: 170px;
    background: linear-gradient(160deg, #8da56a 0%, #b9713f 55%, #5e4a2e 100%);
  }
  .offer-band {
    position: absolute;
    left: 0; top: 380px;
    width: 100%; height: 70px;
    background: linear-gradient(90deg, transparent 0%, rgba(140,198,63,.55) 30%, rgba(140,198,63,.55) 70%, transparent 100%);
  }
  .offer {
    position: absolute;
    top: 378px;
    left: 380px;
    width: 200px;
    text-align: center;
  }
  .offer-amount {
    font-family: "Roboto Condensed", Arial, sans-serif;
    font-weight: 700;
    font-size: 34px;
    color: var(--ink);
  }
  .offer-amount small { font-size: 24px; }
  .offer-note {
    font-size: 18px;
    color: var(--white);
  }
  .front-base {
    position: absolute;
    left: 0; bottom: 0;
    width: 100%; height: 46px;
    background: linear-gradient(180deg, var(--leaf-deep), var(--leaf-dark));
    opacity: .75;
  }
  /* ---------- Back ---------- */
  .card-back {
    top: 624px;
    background: var(--white);
  }
  .back-panel {
    position: absolute;
    left: 0; top: 0;
    width: 500px; height: 100%;
    background: linear-gradient(180deg, var(--white) 0%, var(--leaf-light) 45%, var(--leaf-mid) 100%);
  }
  .back-title {
    position: absolute;
    left: 22px; top: 50px;
    font-family: "Roboto Condensed", Arial, sans-serif;
    font-weight: 700;
    font-size: 26px;
    color: var(--ink);
  }
  .back-copy {
    position: absolute;
    left: 22px; top: 88px;
    width: 470px;
    font-size: 17px;
    line-height: 1.3;
    color: var(--ink-soft);
  }
  .contact-tab {
    position: absolute;
    left: 22px; top: 200px;
    width: 150px; height: 30px;
    background: var(--leaf-dark);
    color: var(--white);
    font-family: "Roboto Condensed", Arial, sans-serif;
    font-weight: 700;
    font-size: 20px;
    line-height: 30px;
    padding-left: 12px;
  }
  .contact-list {
    position: absolute;
    left: 24px; top: 242px;
    list-style: none;
    font-size: 15px;
    line-height: 25px;
    color: var(--ink-soft);
  }
  .contact-list li { display: flex; align-items: center; gap: 8px; }
  .contact-list svg { width: 14px; height: 14px; fill: var(--ink-soft); }
  .partner-badge {
    position: absolute;
    left: 330px; top: 196px;
    width: 120px; height: 120px;
    border-radius: 50%;
    background: radial-gradient(circle, var(--leaf-deep), var(--leaf-dark));
    border: 4px solid #c59b3a;
  }
  .photo-owner {
    left: 22px; top: 372px; width: 176px; height: 140px;
    background: linear-gradient(170deg, #7ea35a 0%, #b99a7a 55%, #55753a 100%);
  }
  .photo-panda-back {
    left: 250px; top: 350px; width: 200px; height: 160px;
    background: radial-gradient(circle at 50% 50%, var(--panda) 0%, var(--panda-dark) 55%, var(--photo-green) 100%);
  }
  .address-side {
    position: absolute;
    left: 500px; top: 0;
    width: 320px; height: 100%;
  }
  .stamp-box {
    position: absolute;
    right: 34px; top: 34px;
    width: 86px; height: 100px;
    border: 2px solid var(--line);
  }
  .address-line {
    position: absolute;
    left: 30px;
    width: 256px;
    border-top: 2px solid var(--line);
  }
</style>
</head>
<body>

<section class="card card-front" aria-label="Postcard front">
  <div class="leaf-border" role="img" aria-label="Bamboo leaves framing the card edges"></div>

  <div class="brand-front">
    <span class="brand-mark"></span>
    <span class="brand-name">Willow Wes</span>
  </div>

  <h1 class="tagline">Stripped and shipped<br>super-fresh (?)</h1>

  <div class="offer-band"></div>
  <div class="photo photo-panda-front" role="img" aria-label="Photo of a red panda among bamboo"></div>
  <div class="photo photo-feeding" role="img" aria-label="Photo of red pandas eating fresh bamboo"></div>

  <div class="offer">
    <div class="offer-amount">10% <small>OFF</small></div>
    <div class="offer-note">Your first order</div>
  </div>

  <div class="front-base"></div>
</section>

<section class="card card-back" aria-label="Postcard back">
  <div class="back-panel"></div>

  <h2 class="back-title">Willow Wes's</h2>
  <p class="back-copy">Feel the Loam, is the foremost supplier of live-bamboo for residential and commercial applications, both indoor and outdoor. We install, remove, maintain bamboo.</p>

  <div class="contact-tab">Contact</div>
  <ul class="contact-list">
    <li><svg viewBox="0 0 24 24"><path d="M6.6 10.8a15 15 0 0 0 6.6 6.6l2.2-2.2a1 1 0 0 1 1-.25 11.4 11.4 0 0 0 3.6.57 1 1 0 0 1 1 1V20a1 1 0 0 1-1 1A17 17 0 0 1 3 4a1 1 0 0 1 1-1h3.5a1 1 0 0 1 1 1c0 1.25.2 2.45.57 3.57a1 1 0 0 1-.25 1z"/></svg>555-014-2290</li>
    <li><svg viewBox="0 0 24 24"><path d="M2 5h20v14H2z M2 5l10 8 10-8" fill="none" stroke="currentColor" stroke-width="2"/></svg>ww@canemail.example</li>
    <li><svg viewBox="0 0 24 24"><circle cx="12" cy="12" r="9" fill="none" stroke="currentColor" stroke-width="2"/><path d="M3 12h18M12 3c3 3 3 15 0 18M12 3c-3 3-3 15 0 18" fill="none" stroke="currentColor" stroke-width="1.5"/></svg>icanecrafter.example</li>
    <li><svg viewBox="0 0 24 24"><path d="M2 5h20v14H2z M2 5l10 8 10-8" fill="none" stroke="currentColor" stroke-width="2"/></svg>FeelTheLoam@loammail.example</li>
  </ul>

  <div class="partner-badge" role="img" aria-label="Round company badge"></div>
  <div class="photo photo-owner" role="img" aria-label="Photo of Willow Wes with bamboo"></div>
  <div class="photo photo-panda-back" role="img" aria-label="Photo of a red panda"></div>

  <div class="address-side">
    <div class="stamp-box"></div>
    <div class="address-line" style="top:250px"></div>
    <div class="address-line" style="top:300px"></div>
    <div class="address-line" style="top:350px"></div>
    <div class="address-line" style="top:400px"></div>
  </div>
</section>

</body>
</html>
```